"Oral Surgery Office needs a Business Card Design with Logo"

We need a logo design and business card. The name of the office is Tassingford Oral Surgery & Implant Center. The final design should communicate uniqueness as well as highly class office. The business card should emphasize power. I included the current business card below. Please design something unique

Target Market(s)

Dentists & Patients

Industry/Entity Type

Dental

Contact Information for Business Card

Unique Design to show success, prestige, Style, unmatched performance

Font styles to use
Serif

Colors
1b1b1b
ffffff
0556a4

Requirements
Must have
• Bussiness Name, Doctor's Name, Website, phone and Fax, email, office address
• Color should be either Black and White or Blue and White
Nice to have
• Clean look
Should not have
• the business card shouldn't be too busy. I feel like the old business card was too busy

```html
<!DOCTYPE html>
<html lang="en">
<head>
<meta charset="utf-8">
<title>Tassingford Oral Surgery &amp; Implant Center – Business Card</title>
<link href="https://fonts.googleapis.com/css2?family=Cormorant+Garamond:wght@600&family=Lora:wght@400;700&display=swap" rel="stylesheet">
<style>
  :root {
    --page-bg: #ececec;
    --card-white: #ffffff;
    --blue: #0556a4;
    --ink: #1b1b1b;
  }
  * { margin: 0; padding: 0; box-sizing: border-box; }
  html, body {
    width: 994px; height: 1200px; overflow: hidden;
    background: var(--page-bg);
    font-family: "Lora", Georgia, serif;
  }
  .card {
    position: absolute;
    width: 754px; height: 458px;
    background: var(--card-white);
    box-shadow: 0 2px 8px rgba(0,0,0,0.18);
    overflow: hidden;
  }
  .card--front { left: 120px; top: 105px; }
  .card--back  { left: 126px; top: 636px; }
  .card__waves { position: absolute; inset: 0; width: 754px; height: 458px; }

  .brand {
    position: absolute;
    display: flex; align-items: center;
    font-family: "Cormorant Garamond", Garamond, serif;
    font-weight: 600;
    color: var(--blue);
    text-transform: uppercase;
    white-space: nowrap;
  }
  .brand__mark { flex: none; border-radius: 50%; background: var(--blue); }
  .brand__name { text-align: center; line-height: 1.1; }
  .brand__first { display: block; }
  .brand__rest { display: block; }

  .card--front .brand { left: 0; width: 754px; top: 56px; justify-content: center; gap: 22px; }
  .card--front .brand__mark { width: 58px; height: 58px; }
  .card--front .brand__first { font-size: 44px; letter-spacing: 10px; margin-right: -10px; }
  .card--front .brand__rest { font-size: 25px; letter-spacing: 0.5px; }

  .card--back .brand { right: 38px; top: 42px; gap: 12px; }
  .card--back .brand__mark { width: 34px; height: 34px; }
  .card--back .brand__first { font-size: 25px; letter-spacing: 6px; margin-right: -6px; }
  .card--back .brand__rest { font-size: 14px; letter-spacing: 0.3px; }

  .website {
    position: absolute; left: 0; width: 754px;
    text-align: center; color: var(--blue);
    font-size: 23px; white-space: nowrap;
  }
  .card--front .website { top: 306px; }
  .card--back .website  { top: 398px; }

  .social {
    position: absolute; top: 372px; left: 0; width: 754px;
    display: flex; justify-content: center; align-items: center; gap: 22px;
    font-size: 18px; color: var(--ink); white-space: nowrap;
  }
  .social__item { display: flex; align-items: center; gap: 10px; }
  .social__mark { width: 32px; height: 32px; border-radius: 4px; background: var(--blue); }

  .doctor { position: absolute; left: 74px; top: 94px; }
  .doctor__name { font-size: 22px; font-weight: 700; color: var(--blue); }
  .doctor__specialty { font-size: 19px; color: var(--ink); margin-top: 4px; }

  .contact-list {
    position: absolute; left: 90px; top: 180px;
    list-style: none; color: var(--ink);
    font-size: 22px; line-height: 32px; white-space: nowrap;
  }
  .contact-list li { display: flex; align-items: center; gap: 8px; }
  .contact-list svg { width: 22px; height: 22px; flex: none; }
</style>
</head>
<body>

<section class="card card--front" aria-label="Business card front">
  <svg class="card__waves" viewBox="0 0 754 458" aria-hidden="true">
    <defs>
      <linearGradient id="bandFront" x1="0" y1="0" x2="0" y2="1">
        <stop offset="0" stop-color="#f7f7f8"/>
        <stop offset="1" stop-color="#dcdde0"/>
      </linearGradient>
    </defs>
    <path d="M0,185 C60,280 210,290 420,272 C560,250 680,222 754,268 L754,458 L0,458 Z" fill="url(#bandFront)"/>
    <path d="M0,172 C50,268 210,290 430,271 C230,284 60,276 0,198 Z" fill="var(--blue)"/>
    <path d="M400,276 C560,236 690,212 754,262 L754,284 C690,236 560,246 400,276 Z" fill="var(--ink)"/>
  </svg>

  <div class="brand">
    <span class="brand__mark"></span>
    <span class="brand__name"><span class="brand__first">Tassingford</span><span class="brand__rest">Oral Surgery &amp; Implant Center</span></span>
  </div>

  <div class="website">www.TassingfordOralSurgeryCenter.com</div>

  <div class="social">
    <span class="social__item"><span class="social__mark"></span>Oral Surgeon</span>
    <span class="social__item"><span class="social__mark"></span>Tassingford Oral Surgery and Implant Center</span>
  </div>
</section>

<section class="card card--back" aria-label="Business card back">
  <svg class="card__waves" viewBox="0 0 754 458" aria-hidden="true">
    <defs>
      <linearGradient id="bandBack" x1="0" y1="0" x2="0" y2="1">
        <stop offset="0" stop-color="#f7f7f8"/>
        <stop offset="1" stop-color="#dcdde0"/>
      </linearGradient>
    </defs>
    <path d="M0,352 C80,318 200,320 330,348 C500,380 680,352 754,272 L754,458 L0,458 Z" fill="url(#bandBack)"/>
    <path d="M0,360 C70,318 200,316 330,346 C210,326 90,330 0,374 Z" fill="var(--ink)"/>
    <path d="M300,342 C480,378 680,350 754,262 L754,282 C690,360 480,384 300,342 Z" fill="var(--blue)"/>
  </svg>

  <div class="brand">
    <span class="brand__mark"></span>
    <span class="brand__name"><span class="brand__first">Tassingford</span><span class="brand__rest">Oral Surgery &amp; Implant Center</span></span>
  </div>

  <div class="doctor">
    <div class="doctor__name">DR. Marek Halloway, D.D.S.</div>
    <div class="doctor__specialty">Oral and Maxillofacial Surgery</div>
  </div>

  <ul class="contact-list">
    <li>
      <svg viewBox="0 0 24 24" aria-label="Address"><path d="M3 11 L12 4 L21 11 Z M5 11 H19 V20 H5 Z" fill="var(--blue)"/><rect x="8" y="13" width="3" height="3" fill="#fff"/><rect x="13" y="13" width="3" height="7" fill="#fff"/></svg>
      2740 Linden Row, Tassingford, NY 11902
    </li>
    <li>
      <svg viewBox="0 0 24 24" aria-label="Phone"><path d="M6 3 L9 3 L10.5 7.5 L8.5 9.5 C9.5 12 12 14.5 14.5 15.5 L16.5 13.5 L21 15 L21 18 C21 19.5 19.5 21 18 21 C10 20 4 14 3 6 C3 4.5 4.5 3 6 3 Z" fill="var(--blue)"/></svg>
      555-214-4700
    </li>
    <li>
      <svg viewBox="0 0 24 24" aria-label="Fax"><rect x="7" y="3" width="10" height="6" fill="none" stroke="var(--blue)" stroke-width="1.6"/><rect x="3" y="9" width="18" height="8" rx="1" fill="var(--blue)"/><rect x="7" y="14" width="10" height="7" fill="#fff" stroke="var(--blue)" stroke-width="1.6"/></svg>
      555-214-5006
    </li>
    <li>
      <svg viewBox="0 0 24 24" aria-label="Email"><rect x="3" y="6" width="18" height="12" fill="none" stroke="var(--blue)" stroke-width="1.8"/><path d="M3 6 L12 13 L21 6" fill="none" stroke="var(--blue)" stroke-width="1.8"/></svg>
      TassingfordOralSurgeryCenter.com
    </li>
  </ul>

  <div class="website">www.TassingfordOralSurgeryCenter.com</div>
</section>

</body>
</html>
```